Web Page - finishing touches

Take my existing rough draft and make it look professional. The components are in place but the page needs a creative touch with a crisp look, professional fonts, and attractive colors.

We are a bathroom remodeling company whose primary customers are 50 + years old and conservative. Our goal for the home page is to get them to request a free estimate, request a Buyer's Guide, or subscribe to our newsletter.
Updates

Project Deadline Extended
Reason: Our website design deadline has been extended by two days. Thanks!

Target Market(s)

Homeowners 50 + years old

Industry/Entity Type

Conservative

Requirements
Must have
• The TILE-NOVA logo can not be changed.

Everything on the rough draft must be included in the finished design.

```html
<!DOCTYPE html>
<html lang="en">
<head>
<meta charset="utf-8">
<title>TILE-NOVA Bathroom Remodeling</title>
<link href="https://fonts.googleapis.com/css2?family=Dosis:wght@500;600;700&family=Fenix&family=Merriweather:ital,wght@1,700&family=Open+Sans:ital,wght@0,400;0,600;1,400&display=swap" rel="stylesheet">
<style>
:root{
  --green:#79b64a;
  --green-soft:#f1f8ea;
  --ink:#333;
  --text:#555;
  --nav-band:#c8d0d5;
  --nav-strip:#dde3e6;
  --field:#92a3ab;
  --section:#eef1f2;
  --footer:#363636;
  --bar:#000;
  --brand-red:#d32a2a;
  --light-field:#d0d5d8;
}
*{box-sizing:border-box;margin:0;padding:0}
html,body{width:1047px;height:1200px;overflow:hidden;background:#fff}
.page{position:relative;width:1200px;height:1376px;transform:scale(.8725);transform-origin:0 0;font-family:"Open Sans",sans-serif;color:var(--text)}
.abs{position:absolute}
.brand{left:130px;top:52px;display:flex;align-items:center;gap:12px;font-family:"Dosis",sans-serif;font-weight:700;font-size:50px;color:var(--brand-red);letter-spacing:1px}
.brand-dot{width:18px;height:18px;border-radius:50%;background:var(--brand-red)}
.call{right:138px;top:44px;font-family:"Dosis",sans-serif;font-size:20px;font-weight:600;color:var(--ink);display:flex;align-items:center;gap:6px}
.call .dot{width:11px;height:11px;border-radius:50%;background:#ccc}
.call .num{color:var(--green);font-weight:500}
.nav{left:123px;top:151px;width:942px;height:40px;background:var(--nav-band);border-bottom:8px solid var(--nav-strip)}
.nav a,.bottom-nav a{position:absolute;font-family:"Dosis",sans-serif;font-weight:600;font-size:19px;color:#fff;text-decoration:none;white-space:nowrap}
.nav a{top:6px}
.nav a.active{color:var(--green)}
.hero-photo{left:151px;top:232px;width:451px;height:318px;border:2px solid #222;background:linear-gradient(120deg,#d8c3a4,#eadbc4 45%,#c9b092 80%,#a98d70)}
.hero-banner{left:152px;top:414px;width:362px;height:104px;background:rgba(121,182,74,.88);color:#fff;font-family:"Merriweather",serif;font-style:italic;font-weight:700;font-size:23px;line-height:26px;padding:21px 0 0 38px}
.pager{left:346px;top:557px;display:flex;gap:8px}
.pager span{width:13px;height:13px;border-radius:50%;border:1.5px solid #444}
.pager span.on{background:#ddd}
.intro{left:611px;top:230px;width:458px;height:319px;background:var(--green-soft)}
.heading{font-family:"Fenix",serif;color:var(--ink);display:flex;align-items:center;gap:4px}
.heading::before{content:"";width:10px;height:10px;border-radius:50%;background:var(--green)}
.intro .heading{position:absolute;left:12px;top:4px;font-size:23px}
.perks{position:absolute;left:28px;top:50px;list-style:none;font-style:italic;font-size:15.5px;line-height:26.5px}
.perks li::before{content:"";display:inline-block;width:6px;height:6px;border-radius:50%;background:var(--green);margin-right:4px;vertical-align:middle}
.intro p{position:absolute;left:15px;top:163px;width:420px;font-size:15.5px;line-height:18px}
.btn{position:absolute;height:27px;background:var(--green);color:#fff;font-size:16px;line-height:27px;padding:0 8px;border-radius:2px;white-space:nowrap}
.contact{left:125px;top:595px;width:940px;height:434px;background:var(--section)}
.contact .heading{position:absolute;left:11px;top:8px;font-size:26px}
.field{position:absolute;left:9px;width:458px;height:28px;background:var(--field);border-radius:3px;color:#fff;font-weight:600;font-size:15px;padding:4px 7px}
.vanity-photo{left:642px;top:651px;width:377px;height:274px;border:3px solid #222;background:linear-gradient(100deg,#b69a78,#4a2a1c 25%,#5c3a28 55%,#d9cbb3 80%,#8f7a64)}
.caption{left:645px;top:937px;width:380px;font-size:15.5px;line-height:18px}
.footer{left:0;top:1051px;width:1200px;height:261px;background:var(--footer);color:#fff}
.footer .heading{position:absolute;top:16px;font-size:26px;color:#fff}
.footer .small{position:absolute;font-size:13px;line-height:15px}
.quote{left:131px;top:56px;width:302px;color:#ccc;font-size:13.5px!important}
.by{left:205px;top:145px;font-style:italic;color:#ccc}
.guide{left:132px;top:172px;font-size:16px;line-height:18px;position:absolute}
.nl-field{position:absolute;left:446px;width:297px;height:27px;background:var(--light-field);color:#fff;font-weight:600;font-size:15px;padding:3px 7px}
.phone{left:765px;top:111px;font-size:22px;position:absolute}
.badges{left:945px;top:1154px}
.bottom-nav{left:0;top:1312px;width:1200px;height:64px;background:var(--bar)}
.bottom-nav a{top:11px}
.sep{position:absolute;top:11px;width:2px;height:27px;background:var(--green)}
</style>
</head>
<body>
<div class="page">
  <div class="abs brand"><span class="brand-dot"></span>TILE-NOVA</div>
  <div class="abs call"><span class="dot"></span>Call Us Today <span class="num">: 919 555 0142</span></div>

  <nav class="abs nav">
    <a class="active" style="left:17px">Home</a>
    <a style="left:140px">About Us</a>
    <a style="left:285px">Design Photos</a>
    <a style="left:448px">Products</a>
    <a style="left:579px">Showroom</a>
    <a style="left:730px">Contact Us</a>
    <a style="left:883px">Blog</a>
  </nav>

  <div class="abs hero-photo" role="img" aria-label="Remodeled bathroom with glass walk-in shower and beige tile"></div>
  <div class="abs hero-banner">Get free design ideas and<br>estimates guarandeed.</div>
  <div class="abs pager"><span class="on"></span><span></span><span></span><span></span></div>

  <section class="abs intro">
    <h2 class="heading">Bathroom remodeling by Tile-Nova</h2>
    <ul class="perks">
      <li>Free design ideas and estimates</li>
      <li>Full service bathroom remodeler</li>
      <li>A+ Rating by the Trusted Trade Council</li>
      <li>17 Years of experience</li>
    </ul>
    <p>Whether you need a simple bathtub replacement or a complete bathroom remodel, we can help. We're the Harlan Family and we've remodeled over 8,000 bathrooms in the past 17 years. We offer affordable bathroom remodeling solutions for any budget with attractive payment options. Call us today</p>
    <span class="btn" style="left:19px;top:286px">Learn More</span>
  </section>

  <section class="abs contact">
    <h2 class="heading">Contact Us</h2>
    <div class="field" style="top:59px">Email</div>
    <div class="field" style="top:95px">Tel</div>
    <div class="field" style="top:131px">Subject</div>
    <div class="field" style="top:168px;height:146px">Content</div>
    <span class="btn" style="left:9px;top:330px;width:97px;padding-left:17px">Submit</span>
  </section>
  <div class="abs vanity-photo" role="img" aria-label="Bathroom with dark wood double vanity and wall mirror, video preview"></div>
  <div class="abs caption">Can Tile-Nova remodel my bathroom in one-day like other companies advertise?</div>
  <span class="btn" style="left:642px;top:979px">Learn More</span>

  <footer class="abs footer">
    <h2 class="heading" style="left:135px">Testimonials</h2>
    <p class="small quote">"Dale, our installer, is a highly skilled professional. He was courteous, gave attention to detail, adn is the model of what a customer would want in the service he provided. Please THANK him again for his workmanship and customer service."</p>
    <p class="small by">Glen and Ruth Mercer, Oak Hollow</p>
    <p class="guide">Free buyer's GUide for Bathroom<br>Remodeling</p>
    <span class="btn" style="left:129px;top:211px">Get it now</span>

    <h2 class="heading" style="left:445px">Newsletter</h2>
    <p class="small" style="left:445px;top:57px;width:290px">Subscribe to our Newsletter Discounts and Special Offers, Tips, Interesting Articles, and more...</p>
    <div class="nl-field" style="top:122px">Email</div>
    <div class="nl-field" style="top:158px">Name</div>
    <span class="btn" style="left:446px;top:200px;width:97px;padding-left:17px">Submit</span>

    <h2 class="heading" style="left:764px">Contact Details</h2>
    <p class="small" style="left:765px;top:57px">Have a question? We can help.<br>E-mail us or give us a call. We'll respond quickly.</p>
    <p class="phone">910-555-0187</p>
    <span class="btn" style="left:764px;top:160px;width:97px;padding-left:17px">Contact</span>
  </footer>
  <svg class="abs badges" width="125" height="142" viewBox="0 0 125 142" aria-hidden="true">
    <circle cx="35" cy="36" r="32" fill="#7fb2cf" stroke="#fff" stroke-width="2"/>
    <rect x="77" y="1" width="43" height="70" rx="3" fill="#2f6f98" stroke="#fff" stroke-width="1"/>
    <circle cx="2" cy="123" r="17" fill="#d5d5d5" transform="translate(0 0)"/>
  </svg>
  <svg class="abs" style="left:928px;top:1258px" width="135" height="38" viewBox="0 0 135 38" aria-hidden="true">
    <circle cx="19" cy="19" r="17" fill="#d5d5d5"/>
    <circle cx="68" cy="19" r="17" fill="#d5d5d5"/>
    <circle cx="116" cy="19" r="17" fill="#d5d5d5"/>
  </svg>

  <nav class="abs bottom-nav">
    <a style="left:140px">Home</a><span class="sep" style="left:225px"></span>
    <a style="left:263px">About Us</a><span class="sep" style="left:370px"></span>
    <a style="left:408px">Design Photos</a><span class="sep" style="left:540px"></span>
    <a style="left:571px">Products</a><span class="sep" style="left:669px"></span>
    <a style="left:702px">Showroom</a><span class="sep" style="left:818px"></span>
    <a style="left:853px">Contact Us</a><span class="sep" style="left:971px"></span>
    <a style="left:1006px">Blog</a>
  </nav>
</div>
</body>
</html>
```